Rebrand of 3 bottle labels for nail polish brand

The task is to make a rebranding of our current gel nail polish bottle design. We have become one of the leading european nail polish brand, so we want to improve the quality of the label design to a more scandinavian and minimalistic bottle design, which stille has to be recognisable and unique.

We have attached a more detailed description of the rebranding instructions for our gel polish bottles called "bottle task".
Updates

The Labels should not be just Black and White as stated. But should be mainly Black and White and then some of our color as explained in the uploaded file.

Target Market(s)

Girls and women age 18-55 Northern Europe

Industry/Entity Type

Cosmetic/ Nail Gel Polish

Colors

Designer to choose only greyscale colors for use in the design.

Requirements
Must have
• See attched design instruction
Nice to have
• Moderne, Minimalist, Recognizable and Unique look
Should not have
• Too many elements, too busy design

```html
<!DOCTYPE html>
<html lang="en">
<head>
<meta charset="utf-8">
<title>Solvik label set</title>
<link rel="stylesheet" href="https://fonts.googleapis.com/css2?family=Quicksand:wght@400;500;600;700&family=Roboto:wght@400;700&display=swap">
<style>
  :root {
    --bg: #ece7e8;
    --black: #000000;
    --leaf-dark: #262626;
    --leaf-mid: #333333;
    --rose: #d4a0a7;
    --rose-soft: #dcb0b6;
    --white: #ffffff;
    --grey-text: #c9c9c9;
  }
  * { margin: 0; padding: 0; box-sizing: border-box; }
  html, body { width: 1200px; height: 3266px; overflow: hidden; background: var(--bg); }
  body { position: relative; font-family: "Roboto", Arial, sans-serif; color: var(--white); }

  .label { position: absolute; background: var(--black); overflow: hidden; }
  .label--color { left: 82px; top: 610px; width: 1034px; height: 275px; }
  .label--base  { left: 82px; top: 959px; width: 1034px; height: 275px; }
  .label--remover { left: 203px; top: 2083px; width: 793px; height: 429px; }

  .front { position: absolute; left: 0; top: 0; height: 100%; }
  .label--color .front, .label--base .front { width: 518px; }
  .back {
    position: absolute; top: 0; right: 0; height: 100%;
    background: linear-gradient(135deg, var(--leaf-dark), var(--leaf-mid) 50%, var(--leaf-dark));
    display: flex; flex-direction: column; align-items: center; justify-content: center;
    text-align: center; padding: 0 70px;
  }
  .label--color .back, .label--base .back { width: 516px; }

  .brand {
    position: absolute; text-align: center; text-transform: uppercase;
    font-family: "Quicksand", sans-serif; font-weight: 600;
    color: var(--white); letter-spacing: 10px; line-height: 1;
  }
  .label--color .brand, .label--base .brand { left: 160px; width: 290px; top: 44px; font-size: 36px; }

  .product-title {
    position: absolute; left: 160px; width: 280px; text-align: center;
    font-family: "Quicksand", sans-serif; font-size: 22px; letter-spacing: 1.5px; top: 103px;
  }
  .product-title strong { font-weight: 700; }
  .product-sub {
    position: absolute; left: 160px; width: 280px; text-align: center; top: 133px;
    font-family: "Quicksand", sans-serif; font-size: 14px; letter-spacing: 1.5px; color: var(--grey-text);
  }
  .vegan-mark { position: absolute; left: 291px; top: 178px; width: 16px; height: 16px; border-radius: 50%; background: var(--white); }
  .vegan {
    position: absolute; left: 160px; width: 280px; text-align: center; top: 215px;
    font-family: "Quicksand", sans-serif; font-size: 14px; font-weight: 600; letter-spacing: 0.5px;
  }
  .url {
    position: absolute; left: 160px; width: 280px; text-align: center; top: 242px;
    font-family: "Quicksand", sans-serif; font-size: 13px; letter-spacing: 0.5px;
  }
  .volume {
    position: absolute; writing-mode: vertical-rl; transform: rotate(180deg);
    font-family: "Roboto", sans-serif; font-size: 12px; font-weight: 700; letter-spacing: 0.5px;
  }
  .label--color .volume, .label--base .volume { left: 488px; top: 180px; }

  .shade-bar { position: absolute; left: 79px; top: 0; width: 14px; height: 90px; background: var(--rose); }
  .shade-tag {
    position: absolute; writing-mode: vertical-rl; transform: rotate(180deg);
    font-family: "Roboto", sans-serif; font-size: 14px; letter-spacing: 1px; font-style: italic;
  }
  .label--color .shade-tag { left: 80px; top: 102px; }
  .shade-number { position: absolute; font-family: "Quicksand", sans-serif; font-weight: 500; font-size: 48px; line-height: 1; }
  .label--color .shade-number { left: 45px; top: 212px; }

  .shade-panel {
    position: absolute; left: 0; top: 0; width: 91px; height: 100%;
    background: linear-gradient(160deg, var(--rose-soft), var(--rose));
  }
  .label--base .shade-tag { left: 48px; top: 130px; font-weight: 700; }
  .label--base .shade-number { left: 22px; top: 212px; }

  .copy { font-size: 8.5px; line-height: 1.55; }
  .copy b { font-weight: 700; }
  .made { font-size: 8.5px; font-weight: 700; margin-top: 12px; letter-spacing: 0.5px; }
  .icons { display: flex; gap: 10px; margin: 6px 0 10px; }
  .icons svg { width: 20px; height: 20px; }
  .maker { font-size: 8.5px; font-weight: 700; line-height: 1.5; }

  .label--remover .front { width: 405px; }
  .remover-top {
    position: absolute; left: 0; top: 0; width: 100%; height: 165px;
    background: linear-gradient(160deg, var(--rose-soft), var(--rose));
  }
  .remover-bottom {
    position: absolute; left: 0; top: 165px; width: 100%; height: 264px;
    background: linear-gradient(135deg, var(--leaf-dark), var(--leaf-mid) 50%, var(--leaf-dark));
  }
  .label--remover .brand { left: 40px; width: 340px; top: 64px; font-size: 40px; }
  .remover-title {
    position: absolute; left: 40px; width: 330px; top: 210px; text-align: center;
    font-family: "Quicksand", sans-serif; font-size: 22px; letter-spacing: 2.5px; line-height: 1.35; font-weight: 500;
  }
  .label--remover .shade-number { left: 182px; top: 305px; font-size: 54px; }
  .label--remover .url { left: 40px; width: 330px; top: 393px; font-size: 17px; color: var(--rose); letter-spacing: 1px; }
  .label--remover .volume { left: 367px; top: 330px; font-size: 13px; }
  .label--remover .back { width: 388px; background: var(--black); padding: 0 60px; }
  .label--remover .copy { font-size: 8.5px; line-height: 1.45; }
  .label--remover .copy b { display: block; margin-top: 9px; }
  .label--remover .copy b:first-child { margin-top: 0; }
</style>
</head>
<body>

<svg width="0" height="0" style="position:absolute" aria-hidden="true">
  <defs>
    <symbol id="icon-recycle" viewBox="0 0 20 20"><path d="M10 2 L14 8 H6 Z M3 16 L7 10 L9 15 Z M17 16 H11 L14 10 Z" fill="#fff"/></symbol>
    <symbol id="icon-warn" viewBox="0 0 20 20"><path d="M10 1 L19 10 L10 19 L1 10 Z" fill="none" stroke="#fff" stroke-width="1.6"/><rect x="9.2" y="5" width="1.6" height="7" fill="#fff"/><rect x="9.2" y="13.5" width="1.6" height="1.6" fill="#fff"/></symbol>
    <symbol id="icon-jar" viewBox="0 0 20 20"><rect x="4" y="6" width="12" height="12" rx="1.5" fill="none" stroke="#fff" stroke-width="1.6"/><rect x="5" y="2" width="10" height="3" fill="#fff"/></symbol>
    <symbol id="icon-bin" viewBox="0 0 20 20"><rect x="5" y="5" width="10" height="13" fill="none" stroke="#fff" stroke-width="1.6"/><rect x="3" y="3" width="14" height="1.6" fill="#fff"/><path d="M8 8 V15 M12 8 V15" stroke="#fff" stroke-width="1.4"/></symbol>
  </defs>
</svg>

<section class="label label--color">
  <div class="front">
    <div class="shade-bar"></div>
    <div class="shade-tag">COLOR NAME</div>
    <div class="shade-number">21</div>
    <div class="brand">Solvik</div>
    <div class="product-title"><strong>COLOR</strong> COAT</div>
    <div class="product-sub">SOAL OFF UV / LED</div>
    <div class="vegan-mark"></div>
    <div class="vegan">VEGAN FORMULA</div>
    <div class="url">solvik.example</div>
    <div class="volume">15ml ℮ 0.5oz</div>
  </div>
  <div class="back" role="img" aria-label="Dark grey leaf pattern behind usage text">
    <p class="copy"><b>DIRECTIONS FOR USE (ENG):</b> Solvik Color Coat must be applied in thin layers and cured in one of our Solvik Lamps.<br>
    <b>ANVENDELSE (DK):</b> Solvik Farver skal påføres i tynde lag og hærdes i en af vores Solvik Lamper.<br>
    <b>CAUTION (ENG):</b> Keep out of reach of children. Discontinue use if irritation occurs. Avoid direct sunlight or extreme exposure to LED or UV Light.<br>
    <b>ADVARSEL (DK):</b> Opbevar utilgængeligt for børn. Stop din behandling, hvis produktet forudsager irritation. Undgå direkte sollys eller udsættelse for LED eller UV.<br>
    <b>INGREDIENTS:</b> Acrylates Copolymer, Acrylated Aliphatic Urethane, Cellulose Acetate Butanoate, Dimethicone, Ceresine, wax , Pigment Red, Carbon Black, Titanium dioxide, CI 77891</p>
    <p class="made">MADE IN EUROPE</p>
    <div class="icons"><svg><use href="#icon-recycle"/></svg><svg><use href="#icon-warn"/></svg><svg><use href="#icon-jar"/></svg><svg><use href="#icon-bin"/></svg></div>
    <p class="maker">Nordlys Partners ApS - Fjordvej 14, 4100 Ringholm,<br>Denmark</p>
  </div>
</section>

<section class="label label--base">
  <div class="front">
    <div class="shade-panel" role="img" aria-label="Rose leaf pattern panel"></div>
    <div class="shade-tag">FLEXIBLE</div>
    <div class="shade-number">01</div>
    <div class="brand">Solvik</div>
    <div class="product-title"><strong>BASE</strong> COAT</div>
    <div class="product-sub">SOAL OFF UV / LED</div>
    <div class="vegan-mark"></div>
    <div class="vegan">VEGAN FORMULA</div>
    <div class="url">solvik.example</div>
    <div class="volume">15ml ℮ 0.5oz</div>
  </div>
  <div class="back" role="img" aria-label="Dark grey leaf pattern behind usage text">
    <p class="copy"><b>DIRECTIONS FOR USE (ENG):</b> Solvik Base Coat must be applied in thin layers and cured in one of our Solvik Lamps.<br>
    <b>ANVENDELSE (DK):</b> Solvik Base Coat skal påføres i tynde lag og hærdes i en af vores Solvik Lamper.<br>
    <b>CAUTION (ENG):</b> Keep out of reach of children. Discontinue use if irritation occurs. Avoid direct sunlight or extreme exposure to LED or UV light.<br>
    <b>ADVARSEL (DK):</b> Opbevar utilgængeligt for børn. Stop din behandling, hvis produktet forudsager irritation. Undgå direkte sollys eller udsættelse for LED eller UV.<br>
    <b>INGREDIENTS:</b> Acrylates Copolymer, Acrylated Aliphatic Urethane, Cellulose Acetate Butanoate, Dimethicone, Ceresine, wax , Pigment Red, Carbon Black, Titanium dioxide, CI 77891</p>
    <p class="made">MADE IN EUROPE</p>
    <div class="icons"><svg><use href="#icon-recycle"/></svg><svg><use href="#icon-warn"/></svg><svg><use href="#icon-jar"/></svg><svg><use href="#icon-bin"/></svg></div>
    <p class="maker">Nordlys Partners ApS - Fjordvej 14, 4100 Ringholm,<br>Denmark</p>
  </div>
</section>

<section class="label label--remover">
  <div class="front">
    <div class="remover-top" role="img" aria-label="Rose leaf pattern band"></div>
    <div class="remover-bottom" role="img" aria-label="Dark grey leaf pattern band"></div>
    <div class="brand">Solvik</div>
    <div class="remover-title">GEL POLISH<br>REMOVER</div>
    <div class="shade-number">12</div>
    <div class="url">solvik.example</div>
    <div class="volume">120ml ℮ 4oz</div>
  </div>
  <div class="back">
    <p class="copy"><b>DIRECTIONS FOR USE (ENG):</b>To remove the Solvik polish, soak a lint free wipe with the Solvik Polish Remover, place the saturated wipe on the nail and wrap each nail in foil for 15 minutes. Remove the foil and peel off the gel polish remover. Re-apply if needed. We recommend that you moisturise your nails after this treatment.
    <b>ANVENDELSESGUIDE (DK):</b>For at fjerne Solvik, skal du væde en fnugfri wipe ind i Solvik Neglelakfjerner, hvorefter du placerer din fnugfri wipe på neglen og klemmer den fast i 15 minutter med sølvpapir og negleklips. Fjern herefter foliet og skrab din gellak af med en neglebåndsskubber. Gentag hvis nødvendigt. Vi anbefaler neglеolie efter din behandling.
    <b>CAUTION (ENG):</b>Keep out of the reach of children. Discontinue use if sensitivity or irritation occurs.
    <b>ADVARSEL (DK):</b>Opbevares utilgængeligt for børn. Stop din behandling hvis følsomhed eller irritation opstår.
    <b>INGREDIENTS:</b>Ethyl acetate, n-butyl acetate, Methyl Ethyl ketone, Acetone, Isopropyl alcohol, glycerin.</p>
    <p class="made">MADE IN EUROPE</p>
    <div class="icons"><svg><use href="#icon-recycle"/></svg><svg><use href="#icon-warn"/></svg><svg><use href="#icon-jar"/></svg><svg><use href="#icon-bin"/></svg></div>
    <p class="maker">Nordlys Partners ApS - Fjordvej 14,<br>4100 Ringholm, Denmark</p>
  </div>
</section>

</body>
</html>
```